Quality label design for natural pet care range

Can you create an eye catching label design which will be put onto a range of products?
Initially this is a joint supplement bottle and shampoo for dogs.
We are suppliers of high quality, natural pet supplements and heath care products.
We want to emphasise our brand values, caring, natural and high quality.
Our logo is attached which would need to be included in the design and can be used for colour cues.

The size and specifications have been uploaded to the design brief. Added Monday, January 16, 2017

Reason: There have been some interesting designs but some of the leading ones still need a little refining to meet our needs. I therefore am willing to extend the deadline in order to get exactly what we are looking for. Many thanks

Dog owners in the USA & Canada

Pet Care

• Our logo, barcode and telephone number
• 'Made in the USA' or a stars and stripes flag

```html
<!DOCTYPE html>
<html lang="en">
<head>
<meta charset="utf-8">
<title>Canine Joint Care Label</title>
<link href="https://fonts.googleapis.com/css2?family=Oswald:wght@400;500;600&family=Roboto:wght@400;500;700&display=swap" rel="stylesheet">
<style>
  :root {
    --backdrop: #e6e6e6;
    --label-white: #fbfcfc;
    --ink: #2f3c3b;
    --band-dark: #2c3837;
    --tab-dark: #3d4a4c;
    --band-blue: #8fbadc;
    --band-blue-deep: #7eaed4;
    --paw-tint: #d4ecec;
    --brand-dot: #2fae4b;
    --on-dark: #eef3f4;
    --badge-red: #b8323c;
  }
  * { box-sizing: border-box; margin: 0; padding: 0; }
  html, body { width: 1200px; height: 1028px; overflow: hidden; }
  body {
    background: var(--backdrop);
    position: relative;
    font-family: "Roboto", Arial, sans-serif;
  }
  .label {
    position: absolute;
    left: 240px;
    top: 74px;
    width: 720px;
    height: 880px;
    background: var(--label-white);
    overflow: hidden;
  }
  .brand {
    position: absolute;
    top: 196px;
    left: 0;
    width: 100%;
    display: flex;
    justify-content: center;
    align-items: center;
    gap: 14px;
  }
  .brand-dot {
    width: 26px;
    height: 26px;
    border-radius: 50%;
    background: var(--brand-dot);
  }
  .brand-name {
    font-family: "Oswald", "Arial Narrow", sans-serif;
    font-weight: 600;
    font-size: 44px;
    letter-spacing: 1px;
    color: var(--ink);
    line-height: 1;
  }
  .paw-pattern {
    position: absolute;
    top: 320px;
    left: 90px;
    width: 540px;
    height: 250px;
    background: radial-gradient(ellipse at center, rgba(212,236,236,0.55) 0%, rgba(212,236,236,0) 70%);
  }
  .product-title {
    position: absolute;
    top: 352px;
    left: 0;
    width: 100%;
    text-align: center;
    font-family: "Oswald", "Arial Narrow", sans-serif;
    color: var(--ink);
  }
  .product-kind {
    display: block;
    font-weight: 500;
    font-size: 54px;
    line-height: 1;
    letter-spacing: 1px;
  }
  .product-name {
    display: block;
    font-weight: 500;
    font-size: 112px;
    line-height: 1;
    margin-top: 8px;
    letter-spacing: 0;
  }
  .claim-band {
    position: absolute;
    top: 582px;
    left: 0;
    width: 100%;
    height: 72px;
    background: var(--band-dark);
    color: var(--on-dark);
    display: flex;
    align-items: center;
    justify-content: center;
    font-size: 35px;
    letter-spacing: 1px;
    font-weight: 400;
  }
  .info-band {
    position: absolute;
    top: 654px;
    left: 0;
    width: 100%;
    height: 226px;
    background: linear-gradient(180deg, var(--band-blue-deep) 0%, var(--band-blue) 40%, var(--band-blue) 100%);
  }
  .claim-tab {
    position: absolute;
    top: 0;
    left: 50%;
    transform: translateX(-50%);
    width: 316px;
    height: 50px;
    background: var(--tab-dark);
    color: var(--on-dark);
    border-radius: 0 0 8px 8px;
    display: flex;
    align-items: center;
    justify-content: center;
    font-size: 19px;
    letter-spacing: 1px;
  }
  .volume {
    position: absolute;
    top: 114px;
    left: 0;
    width: 100%;
    text-align: center;
    color: var(--on-dark);
    font-weight: 700;
    font-size: 18px;
    letter-spacing: 1.5px;
  }
  .origin-badge {
    position: absolute;
    top: 72px;
    left: 480px;
    width: 92px;
    height: 82px;
  }
</style>
</head>
<body>
  <main class="label">
    <div class="brand">
      <span class="brand-dot"></span>
      <span class="brand-name">BRIGHTWELL PET</span>
    </div>

    <div class="paw-pattern" role="img" aria-label="Faint scattered paw print pattern"></div>

    <h1 class="product-title">
      <span class="product-kind">CANINE</span>
      <span class="product-name">JOINT CARE</span>
    </h1>

    <div class="claim-band">FORMULATED TO SUPPORT</div>

    <section class="info-band">
      <div class="claim-tab">HEALTHY&nbsp; JOINT FUNCTION</div>
      <p class="volume">4 FL OZ | 118mL</p>
      <svg class="origin-badge" viewBox="0 0 92 82" role="img" aria-label="Made in USA badge">
        <rect x="0" y="0" width="92" height="82" rx="4" fill="var(--badge-red)"/>
      </svg>
    </section>
  </main>
</body>
</html>
```